Fitness Business Card Design Needed

We are looking for a business card design that stands out but is also simple and unique. I like the idea of on one side using the picture of myself with my logo at my feet. I love the texture on the business card so please take that into account when designing. Then on the other side having my contact details. I want it to be clean, modern, and pretty. I am open to designs that allow spot gloss or gold foiling.

Contact Information for Business Card

Space for Name, Phone number, email, and website

```html
<!DOCTYPE html>
<html lang="en">
<head>
<meta charset="utf-8">
<title>Small But Strong Fitness – Business Card</title>
<link rel="stylesheet" href="https://fonts.googleapis.com/css2?family=Montserrat:wght@400;500&family=Roboto:wght@400&display=swap">
<style>
  :root {
    --page: #e6e6e6;
    --card: #4a0000;
    --gold: #d8a654;
    --gold-soft: #b98a3e;
    --white: #ffffff;
    --ink-light: #f3e9e6;
  }
  * { box-sizing: border-box; margin: 0; padding: 0; }
  html, body { width: 1200px; height: 900px; overflow: hidden; }
  body {
    background: var(--page);
    position: relative;
    font-family: "Montserrat", sans-serif;
  }
  .card {
    position: absolute;
    top: 200px;
    width: 310px;
    height: 502px;
    background: var(--card);
    box-shadow: 2px 3px 6px rgba(0,0,0,0.35);
    overflow: hidden;
  }
  .card--front { left: 308px; border-radius: 58px 0 58px 0; }
  .card--back  { left: 641px; border-radius: 58px 58px 0 58px; }

  /* front */
  .trainer-photo {
    position: absolute;
    left: 82px;
    top: 20px;
    width: 214px;
    height: 482px;
    border-radius: 90px 90px 20px 20px;
    background: linear-gradient(180deg, #c9a88a 0%, #d9906f 30%, #d4604a 45%, #c98a6c 60%, #b8745a 100%);
  }
  .front-brand {
    position: absolute;
    left: 30px;
    top: 130px;
    width: 50px;
    height: 280px;
    display: flex;
    align-items: center;
    gap: 10px;
  }
  .front-brand__name {
    writing-mode: vertical-rl;
    transform: rotate(180deg);
    color: var(--gold);
    font-weight: 400;
    font-size: 21px;
    letter-spacing: 3px;
    white-space: nowrap;
  }
  .front-brand__rule {
    width: 1px;
    height: 272px;
    background: var(--gold);
  }

  /* back */
  .back-brand {
    position: absolute;
    top: 58px;
    left: 0;
    width: 100%;
    display: flex;
    flex-direction: column;
    align-items: center;
    gap: 34px;
  }
  .back-brand__mark {
    width: 70px;
    height: 70px;
    border: 1.5px solid var(--gold);
  }
  .back-brand__name {
    color: var(--white);
    font-weight: 400;
    font-size: 17px;
    letter-spacing: 2.4px;
    white-space: nowrap;
  }
  .contact {
    position: absolute;
    top: 314px;
    left: 0;
    width: 100%;
    text-align: center;
    font-family: "Roboto", sans-serif;
  }
  .contact__name {
    color: var(--gold);
    font-size: 18px;
    letter-spacing: 0.6px;
  }
  .contact__role {
    color: var(--ink-light);
    font-size: 13px;
    letter-spacing: 0.4px;
    margin-top: 3px;
  }
  .contact__icons {
    display: flex;
    justify-content: center;
    align-items: center;
    gap: 4px;
    margin-top: 18px;
  }
  .contact__rule { width: 40px; height: 1px; background: var(--gold-soft); margin: 0 6px; }
  .contact__icon { width: 17px; height: 17px; }
  .contact__lines {
    margin-top: 14px;
    color: var(--ink-light);
    font-size: 13.5px;
    line-height: 18.5px;
    letter-spacing: 0.3px;
  }
</style>
</head>
<body>

  <section class="card card--front">
    <div class="trainer-photo" role="img" aria-label="Full-length photo of the trainer in a red bikini, hands on hips"></div>
    <div class="front-brand">
      <span class="front-brand__name">SMALLBUTSTRONG FITNESS</span>
      <span class="front-brand__rule"></span>
    </div>
  </section>

  <section class="card card--back">
    <div class="back-brand">
      <span class="back-brand__mark"></span>
      <span class="back-brand__name">SMALLBUTSTRONG FITNESS</span>
    </div>

    <div class="contact">
      <p class="contact__name">DANIEL HARPER</p>
      <p class="contact__role">MANAGING DIRECTOR</p>
      <div class="contact__icons">
        <span class="contact__rule"></span>
        <svg class="contact__icon" viewBox="0 0 20 20" aria-label="Phone">
          <circle cx="10" cy="10" r="10" fill="var(--gold)"/>
          <path d="M6 8.5h8v4H6z M7.5 8.5c0-2 5-2 5 0" fill="var(--card)" stroke="var(--card)" stroke-width="0.6"/>
        </svg>
        <svg class="contact__icon" viewBox="0 0 20 20" aria-label="Email">
          <circle cx="10" cy="10" r="10" fill="var(--gold)"/>
          <rect x="5" y="6.5" width="10" height="7" fill="var(--card)"/>
          <path d="M5 6.5l5 4 5-4" fill="none" stroke="var(--gold)" stroke-width="0.8"/>
        </svg>
        <svg class="contact__icon" viewBox="0 0 20 20" aria-label="Website">
          <circle cx="10" cy="10" r="10" fill="var(--gold)"/>
          <circle cx="10" cy="10" r="5" fill="none" stroke="var(--card)" stroke-width="1.2"/>
          <path d="M5 10h10 M10 5c-2.5 3-2.5 7 0 10 M10 5c2.5 3 2.5 7 0 10" fill="none" stroke="var(--card)" stroke-width="0.9"/>
        </svg>
        <span class="contact__rule"></span>
      </div>
      <div class="contact__lines">
        <p>044-987 654 321</p>
        <p>HELLO@STRONGSTUDIO.COM</p>
        <p>WWW.STRONGSTUDIO.COM</p>
      </div>
    </div>
  </section>

</body>
</html>
```